Very visible CoWorking Building Sign overlooking downtown LA and 110 freeway

Our building is drab but very visible and in the best location. We need a great sign for our monolith that overlooks downtown LA and the 100 freeway. We are a new CoWorking business and would like to have a few things we do on the sign: private offices, virtual offices, CoWorking Lounge. Everything we have seen is ho-hum. Can you get us noticed? We need people to know what we do and that we are here but in a creative, professional, unique sign.
Target Market(s)
People who have a business in DTLA, remote workers and those who work from home who need a professional address.
Requirements
Must have
- Our logo (which can be somewhat reimagined) which has our address 2740 on it. The three things we focus on: Private Offices, Virtual Offices, CoWorking Lounge. Incorporate some Navy. Readable from several hundred feet away.
Nice to have
- Mural feel? Something inspirational in this crazy COVID times? Graphics? Color block. I like the idea of decorative but it has to be readable as a building sign. The same with the use of colors. Our colors are grays and navy but with a pop of the chartreuse (we have 2 velvet chartreuse chairs in the space). Helpful to view our website: Halvorn2740.com.
Should not have
- Not too graffiti. Keep it professional but unique and wow.

```html
<!DOCTYPE html>
<html lang="en">
<head>
<meta charset="utf-8">
<title>Halvorn 2740 Building Sign</title>
<link rel="stylesheet" href="https://fonts.googleapis.com/css2?family=Abril+Fatface&display=swap">
<style>
  :root {
    --navy: #1b3360;
    --navy-deep: #13264a;
    --gray: #9b9c9f;
    --backdrop: #e8e9eb;
    --white: #ffffff;
  }
  html, body {
    margin: 0;
    width: 1200px;
    height: 561px;
    overflow: hidden;
    background: var(--backdrop);
  }
  .sign {
    position: absolute;
    left: 88px;
    top: 88px;
    width: 1024px;
    height: 384px;
    box-shadow: 4px 6px 10px rgba(0,0,0,0.35);
    overflow: hidden;
    font-family: "Abril Fatface", Georgia, serif;
    color: var(--navy);
  }
  .sign-art {
    position: absolute;
    inset: 0;
  }
  .brand {
    position: absolute;
    left: 62px;
    top: 66px;
    margin: 0;
    font-size: 38px;
    font-weight: 400;
    letter-spacing: 1px;
    line-height: 1;
    white-space: nowrap;
    color: var(--navy);
  }
  .services {
    position: absolute;
    left: 52px;
    top: 168px;
    margin: 0;
    padding: 0;
    list-style: none;
  }
  .service {
    display: flex;
    align-items: center;
    height: 58px;
    font-size: 42px;
    line-height: 1;
    white-space: nowrap;
  }
  .service-icon {
    width: 28px;
    height: 28px;
    margin-right: 12px;
    flex: none;
  }
</style>
</head>
<body>
  <div class="sign">
    <svg class="sign-art" width="1024" height="384" viewBox="0 0 1024 384">
      <defs>
        <linearGradient id="interiorTones" x1="0" y1="0" x2="1" y2="1">
          <stop offset="0" stop-color="#cfd3d6"/>
          <stop offset="0.35" stop-color="#9aa19a"/>
          <stop offset="0.6" stop-color="#8a7a52"/>
          <stop offset="1" stop-color="#6d6248"/>
        </linearGradient>
      </defs>
      <rect class="panel-white" width="1024" height="384" fill="var(--white)"/>
      <rect class="interior-photo" role="img" aria-label="Lounge interior with two chartreuse velvet armchairs, glass side table, round rug and plants"
            x="380" y="0" width="644" height="384" fill="url(#interiorTones)"/>
      <polygon class="accent-stripe" points="662,0 706,0 914,384 870,384" fill="var(--navy)" opacity="0.75"/>
      <polygon class="accent-stripe" points="766,0 1024,0 1024,384 962,384" fill="var(--navy-deep)" opacity="0.72"/>
      <polygon class="accent-stripe-light" points="856,0 900,0 1024,250 1024,330" fill="var(--white)" opacity="0.25"/>
      <polygon class="panel-white-diagonal" points="0,0 390,0 576,384 0,384" fill="var(--white)"/>
      <rect class="divider" x="0" y="152" width="442" height="5" fill="var(--gray)"/>
      <polygon class="base-band" points="0,358 552,358 567,384 0,384" fill="var(--gray)"/>
    </svg>

    <h1 class="brand">HALVORN 2740</h1>

    <ul class="services">
      <li class="service">
        <svg class="service-icon" viewBox="0 0 28 28" aria-hidden="true">
          <circle cx="14" cy="14" r="12" fill="none" stroke="var(--navy)" stroke-width="2.5"/>
          <path d="M7 14h10M13 9l5 5-5 5" fill="none" stroke="var(--navy)" stroke-width="3"/>
        </svg>Private Offices</li>
      <li class="service">
        <svg class="service-icon" viewBox="0 0 28 28" aria-hidden="true">
          <circle cx="14" cy="14" r="12" fill="none" stroke="var(--navy)" stroke-width="2.5"/>
          <path d="M7 14h10M13 9l5 5-5 5" fill="none" stroke="var(--navy)" stroke-width="3"/>
        </svg>Virtual Offices</li>
      <li class="service">
        <svg class="service-icon" viewBox="0 0 28 28" aria-hidden="true">
          <circle cx="14" cy="14" r="12" fill="none" stroke="var(--navy)" stroke-width="2.5"/>
          <path d="M7 14h10M13 9l5 5-5 5" fill="none" stroke="var(--navy)" stroke-width="3"/>
        </svg>CoWorking Lounge</li>
    </ul>
  </div>
</body>
</html>
```